Design business card using existing logo.

PLEASE DO NOT USE "RED WHITE & BLACK" color combo! Thank you.

Try different color combos such as:
- Vintage colors like brown, orange, gold, blue (not all together but a combo of 1 or 3
- Blue, w/ grey, or silver or white, Blue monochromatic can work as well.
- Use monochromatic variations on back (just an idea)

- Include full name, "Quillmark Records" on at least one side.

Target Market(s)

Teens

Industry/Entity Type

Business

Colors
3277b5
ffc214
f04a50
f78f20

```html
<!DOCTYPE html>
<html lang="en">
<head>
<meta charset="utf-8">
<title>Quillmark Records – Business Card</title>
<link href="https://fonts.googleapis.com/css2?family=Lato:wght@400;700&display=swap" rel="stylesheet">
<style>
  :root {
    --brand-blue: #3277b5;
    --brand-orange: #f78f20;
    --paper-white: #ffffff;
    --back-grey: #e8e8e8;
    --pattern-grey: #dedede;
    --text-grey: #555555;
    --stage: #f3f1ee;
  }
  * { margin: 0; padding: 0; box-sizing: border-box; }
  html, body {
    width: 1200px; height: 900px; overflow: hidden;
    background: var(--stage);
    font-family: "Lato", sans-serif;
  }
  .canvas { position: relative; width: 1200px; height: 900px; }

  /* Front card */
  .card-front {
    position: absolute; left: 148px; top: 98px;
    width: 590px; height: 365px;
    background: var(--brand-blue);
    overflow: hidden;
    color: var(--paper-white);
  }
  .card-front .accent-panel {
    position: absolute; right: 0; top: 0;
    width: 140px; height: 100%;
    background: var(--brand-orange);
  }
  .card-front .emblem-disc {
    position: absolute; left: 223px; top: -4px;
    width: 372px; height: 372px; border-radius: 50%;
    background: var(--paper-white);
    display: flex; align-items: center; justify-content: center;
  }
  .emblem-name {
    color: var(--brand-orange); font-weight: 700;
    font-size: 34px; line-height: 1.15; text-align: center;
    letter-spacing: 1px;
  }
  .holder-name { position: absolute; left: 31px; top: 38px; font-size: 20px; font-weight: 700; letter-spacing: 0.3px; }
  .holder-title { position: absolute; left: 31px; top: 61px; font-size: 15.5px; font-weight: 400; }
  .address { position: absolute; left: 31px; top: 212px; font-size: 15.5px; line-height: 22px; }
  .contact-list { position: absolute; left: 29px; top: 275px; list-style: none; font-size: 17px; line-height: 23px; }
  .contact-list li { display: flex; align-items: center; gap: 6px; }
  .contact-list svg { width: 17px; height: 17px; flex: none; }

  /* Back card */
  .card-back {
    position: absolute; left: 388px; top: 505px;
    width: 567px; height: 352px;
    background: var(--back-grey);
    overflow: hidden;
  }
  .card-back .pattern-field {
    position: absolute; inset: 0;
    background: linear-gradient(180deg, var(--back-grey), var(--pattern-grey));
  }
  .brand-mark {
    position: absolute; left: 0; right: 0; top: 62px;
    display: flex; flex-direction: column; align-items: center;
  }
  .brand-dot {
    width: 118px; height: 118px; border-radius: 50%;
    background: var(--brand-orange);
  }
  .brand-name {
    margin-top: 22px; color: var(--brand-orange);
    font-weight: 700; font-size: 34px; line-height: 1.05;
    text-align: center; letter-spacing: 1px;
  }
  .web-address {
    position: absolute; left: 0; right: 0; top: 296px;
    text-align: center; color: var(--text-grey);
    font-size: 16px; font-weight: 700; letter-spacing: 1.3px;
  }
</style>
</head>
<body>
<main class="canvas">

  <section class="card-front">
    <div class="accent-panel"></div>
    <div class="emblem-disc">
      <div class="emblem-name">QUILLMARK<br>RECORDS</div>
    </div>

    <h1 class="holder-name">DANIEL MORROW</h1>
    <p class="holder-title">Managing Director</p>

    <p class="address">1234, Address Here<br>Country name, 12345</p>

    <ul class="contact-list">
      <li>
        <svg viewBox="0 0 20 20"><circle cx="10" cy="10" r="10" fill="#fff"/><path d="M7 5.5l1.8 2.2-1 1.2c.7 1.4 1.8 2.5 3.2 3.2l1.2-1 2.2 1.8-1 1.6c-3.6-.4-6.9-3.7-7.2-7.3z" fill="#3277b5"/></svg>
        (044)123456789
      </li>
      <li>
        <svg viewBox="0 0 20 20"><circle cx="10" cy="10" r="10" fill="#fff"/><rect x="5" y="6.5" width="10" height="7" fill="#3277b5"/><path d="M5 6.5l5 4 5-4" fill="none" stroke="#fff" stroke-width="1.2"/></svg>
        info@youremail.com
      </li>
      <li>
        <svg viewBox="0 0 20 20"><circle cx="10" cy="10" r="10" fill="#fff"/><circle cx="10" cy="10" r="5" fill="none" stroke="#3277b5" stroke-width="1.6"/><path d="M5 10h10M10 5v10" stroke="#3277b5" stroke-width="1.2"/></svg>
        www.websitename.com
      </li>
    </ul>
  </section>

  <section class="card-back">
    <div class="pattern-field" role="img" aria-label="Faint repeating brand pattern in light grey"></div>
    <div class="brand-mark">
      <div class="brand-dot"></div>
      <div class="brand-name">QUILLMARK<br>RECORDS</div>
    </div>
    <p class="web-address">www.quillmarkrecords.com</p>
  </section>

</main>
</body>
</html>
```